Palm Crest Engineering Consulting & Training Co., LTD.
Palm Crest
Use standard fonts
Arch. Salim Fathi Benzoura
General Manager
Sawani- Algharbia, District - Tripoli, Libya
palmcrest@mailvane.net
The Arabic company name and address نخيل الساحل للاستشارات والخدمات الهندسية والتدريب ذ.م.م الغربية السواني - طرابلس , ليبيا
The Arabic name and information م. سالم الفتحي بنزورة المدير العام
Brisk Brisk
Ok. Can u give some star rating please. Stationary will be based on business card.
kelvurn kelvurn
I'm ordering Business Cards and Stationery kit :(

```html
<!DOCTYPE html>
<html lang="en">
<head>
<meta charset="utf-8">
<title>Palm Crest — Business Card</title>
<link href="https://fonts.googleapis.com/css2?family=Didact+Gothic&family=Cairo:wght@400;600&display=swap" rel="stylesheet">
<style>
  :root {
    --page-bg: #e9e9eb;
    --card-white: #ffffff;
    --brand-red: #b3242b;
    --ink-dark: #3b3b3d;
    --ink-mid: #6a6a6c;
    --silver-light: #b9b9bb;
    --silver-dark: #4a4a4c;
    --deco-grey: #d4d4d6;
  }
  * { margin: 0; padding: 0; box-sizing: border-box; }
  html, body { width: 1200px; height: 904px; overflow: hidden; }
  body {
    background: var(--page-bg);
    font-family: "Didact Gothic", "Trebuchet MS", sans-serif;
    position: relative;
  }
  .card {
    position: absolute;
    left: 250px;
    width: 700px;
    height: 400px;
    border-radius: 4px;
    box-shadow: 0 6px 18px rgba(0,0,0,0.18);
    overflow: hidden;
  }
  .card-back {
    top: 40px;
    background: linear-gradient(135deg, var(--silver-light) 0%, #8c8c8e 40%, var(--silver-dark) 100%);
    display: flex;
    align-items: center;
    justify-content: center;
  }
  .card-front { top: 464px; background: var(--card-white); }

  .brand { display: flex; align-items: center; gap: 12px; white-space: nowrap; }
  .brand-square { width: 26px; height: 26px; flex: none; }
  .brand-name { font-size: 44px; letter-spacing: 1px; }
  .card-back .brand-square { background: #f2f2f2; }
  .card-back .brand-name { color: #f2f2f2; }

  .card-front .brand { position: absolute; left: 42px; top: 112px; }
  .card-front .brand-square { background: var(--ink-dark); width: 20px; height: 20px; }
  .card-front .brand-name { color: var(--brand-red); font-size: 34px; }

  .contact {
    position: absolute;
    left: 44px;
    top: 196px;
    color: var(--ink-mid);
    font-size: 14px;
    line-height: 1.4;
    white-space: nowrap;
  }
  .contact .person { color: var(--brand-red); font-size: 17px; }
  .contact .role { margin-bottom: 8px; }
  .contact .block { margin-bottom: 8px; }

  .arabic {
    position: absolute;
    left: 300px;
    top: 112px;
    width: 270px;
    direction: rtl;
    text-align: right;
    font-family: "Cairo", "Arial", sans-serif;
    color: var(--ink-mid);
    font-size: 11.5px;
    line-height: 1.55;
  }
  .arabic .person-ar { color: var(--brand-red); font-size: 16px; font-weight: 600; }
  .arabic .role-ar { color: var(--ink-dark); font-size: 12.5px; }

  .side-mark {
    position: absolute;
    right: 20px;
    top: 40px;
    width: 90px;
    height: 190px;
    background: var(--deco-grey);
  }
</style>
</head>
<body>
  <section class="card card-back">
    <div class="brand">
      <span class="brand-square"></span>
      <span class="brand-name">Palm Crest</span>
    </div>
  </section>

  <section class="card card-front">
    <div class="brand">
      <span class="brand-square"></span>
      <span class="brand-name">Palm Crest</span>
    </div>

    <div class="arabic">
      <div class="person-ar">م. سالم الفتحي بنزورة</div>
      <div class="role-ar">المدير العام</div>
      <div>نخيل الساحل للاستشارات والخدمات الهندسية والتدريب ذ.م.م</div>
      <div>الغربية السواني - طرابلس , ليبيا</div>
    </div>

    <div class="side-mark"></div>

    <div class="contact">
      <div class="person">Arch. Salim Fathi Benzoura</div>
      <div class="role">General Manager</div>
      <div class="block">
        <div>Sawani- Algharbia ,</div>
        <div>District - Tripoli, Libya</div>
      </div>
      <div class="block">
        <div>+218915550142</div>
        <div>+218915550187</div>
      </div>
      <div>palmcrest@mailvane.net</div>
    </div>
  </section>
</body>
</html>
```